Small boutique multi-family apartment developer needs premium website design.

We are a growing real estate development company specializing in multi family apartment development. Our company Mireval Stone Development focuses on passive real estate investors looking to maximize their current real estate portfolio by allowing us to develop and reposition their current properties allowing them more cashflow while we are also able to take over the management of their asset in order to ensure optimal performance on a consistent basis.

```html
<!DOCTYPE html>
<html lang="en">
<head>
<meta charset="utf-8">
<title>Mireval Stone Development</title>
<link href="https://fonts.googleapis.com/css2?family=Archivo:wght@600;700;800;900&family=Inter:wght@400;500;600;700&display=swap" rel="stylesheet">
<style>
:root{
  --bg:#f1f6fd;
  --navy:#0a1f40;
  --blue:#0b4fa8;
  --sky:#5aa6f2;
  --ink:#0d1b2e;
  --muted:#6b7480;
  --line:#c9d2dc;
  --white:#ffffff;
}
*{margin:0;padding:0;box-sizing:border-box}
html,body{width:1200px;height:3608px;overflow:hidden}
body{background:var(--bg);font-family:"Inter",sans-serif;color:var(--ink);position:relative}
.abs{position:absolute}
.head{font-family:"Archivo",sans-serif}

/* nav */
.brand{left:90px;top:24px;display:flex;align-items:center;gap:8px;font-weight:700;font-size:11px;line-height:12px;color:var(--navy)}
.brand-mark{width:26px;height:26px;background:var(--navy);border-radius:3px}
.nav{top:30px;display:flex;gap:0;font-size:14px;font-weight:600;color:var(--navy)}
.nav a{position:absolute;text-decoration:none;color:inherit;white-space:nowrap}
.btn-outline{left:1008px;top:20px;width:101px;height:35px;border:1.5px solid var(--navy);border-radius:18px;font-size:14px;font-weight:600;display:flex;align-items:center;justify-content:center;color:var(--navy)}

/* hero */
.hero{left:90px;top:76px;width:1019px;height:666px;background:var(--navy);border-radius:14px;overflow:hidden}
.hero-photo{position:absolute;left:358px;top:0;width:661px;height:666px;background:linear-gradient(135deg,var(--navy) 0%,var(--navy) 20%,#dfe4ea 45%,#f4f6f8 60%,#c9ced5 80%,#e8ebef 100%);clip-path:polygon(35% 18%,62% 12%,100% 40%,100% 100%,0 100%,0 30%)}
.hero-title{left:26px;top:150px;font-size:86px;font-weight:900;line-height:96px;color:var(--white);letter-spacing:1px}
.hero-sub{left:27px;top:368px;font-size:20px;color:var(--white)}
.search{left:26px;top:446px;width:482px;height:70px;background:var(--white);border-radius:10px}
.search-field{position:absolute;top:15px;display:flex;align-items:center;gap:10px}
.ico-ring{width:42px;height:42px;border:1.5px solid var(--navy);border-radius:50%;display:flex;align-items:center;justify-content:center}
.field-label{font-size:10px;color:var(--muted)}
.field-value{font-size:13px;font-weight:700;color:var(--navy);margin-top:4px}
.search-btn{position:absolute;left:374px;top:17px;width:88px;height:35px;border-radius:18px;background:var(--navy);color:var(--white);font-size:14px;font-weight:700;display:flex;align-items:center;justify-content:center}

.section-title{left:0;width:1200px;top:780px;text-align:center;font-size:31px;font-weight:800;color:var(--blue)}

/* about */
.about{left:90px;top:860px;width:1019px;height:470px;background:var(--white);border-radius:14px}
.vert{left:20px;top:225px;transform:rotate(-90deg);transform-origin:left top;font-size:13px;letter-spacing:1px;color:var(--navy);top:272px}
.stat{position:absolute;top:40px}
.stat-num{font-family:"Archivo",sans-serif;font-size:42px;font-weight:800;color:var(--navy)}
.stat-label{font-size:17px;color:var(--navy);margin-top:4px}
.eyebrow{left:86px;top:169px;font-size:13px;font-weight:700;color:var(--blue)}
.about-head{left:86px;top:206px;width:500px;font-size:31px;line-height:37px;font-weight:700;color:var(--navy)}
.btn-dark{background:var(--navy);color:var(--white);border-radius:18px;font-size:13px;font-weight:700;display:flex;align-items:center;justify-content:center}
.feature{left:606px;top:39px;width:327px;height:392px;border-radius:4px;background:linear-gradient(180deg,#dfe9f1 0%,#9ec4d4 45%,#7fb4e6 75%,var(--sky) 100%)}
.feature-tag{left:19px;top:20px;font-size:13px;font-weight:600;color:var(--navy)}
.feature-title{left:0;width:327px;top:252px;text-align:center;font-size:28px;line-height:33px;font-weight:700;color:var(--white)}
.feature-btn{left:112px;top:336px;width:102px;height:33px;border-radius:17px;background:var(--white);font-size:13px;color:var(--navy);display:flex;align-items:center;justify-content:center}
.dot{position:absolute;left:981px;width:11px;height:11px;border-radius:50%;border:1.5px solid var(--navy)}

/* rows */
.row-title{left:90px;font-size:28px;font-weight:700;color:var(--blue)}
.explore{left:976px;width:133px;height:34px;border:1.5px solid var(--navy);border-radius:6px;font-size:13px;font-weight:600;color:var(--navy);display:flex;align-items:center;justify-content:center;gap:6px}
.card{width:326px;height:491px;top:1487px;background:var(--white);overflow:hidden}
.card-photo{width:326px;height:379px}
.card-title{position:absolute;left:13px;font-size:20px;font-weight:600;color:var(--navy)}
.pill{position:absolute;height:26px;border:1.3px solid var(--blue);border-radius:13px;font-size:12px;color:var(--blue);display:flex;align-items:center;gap:5px;padding:0 11px}
.meta{position:absolute;display:flex;align-items:center;gap:6px;font-size:14px;color:var(--navy)}

.news{width:326px;height:326px;top:2135px;overflow:hidden;border-radius:2px}
.news-title{position:absolute;left:20px;font-size:20px;line-height:24px;font-weight:600;color:var(--white)}
.news-meta{position:absolute;left:20px;top:296px;font-size:12px;color:var(--white);display:flex;gap:18px;align-items:center}

/* contact */
.form-card{left:90px;top:2570px;width:499px;height:489px;background:var(--white);border-radius:14px}
.form-title{left:26px;top:30px;font-size:28px;font-weight:700;color:var(--navy)}
.form-sub{left:26px;top:82px;font-size:16px;color:var(--navy)}
.input{position:absolute;border:1.3px solid var(--line);border-radius:4px;font-size:13px;color:#a7aeb7;padding:12px}
.submit{left:26px;top:358px;width:447px;height:42px;border-radius:4px;font-size:14px}
.legal{left:0;width:499px;top:428px;text-align:center;font-size:13px;line-height:22px;color:var(--muted)}
.legal b{font-weight:500;color:var(--navy)}
.inquiry{left:609px;top:2573px;width:500px;font-size:29px;line-height:37px;font-weight:700;color:var(--blue)}
.contact-item{position:absolute;left:609px;display:flex;align-items:center;gap:14px;font-size:17px;color:var(--navy)}
.ci-box{width:46px;height:46px;border:1.5px solid var(--blue);border-radius:4px;display:flex;align-items:center;justify-content:center}

/* footer */
.footer{left:0;top:3140px;width:1200px;height:468px;background:var(--navy);color:var(--white)}
.f-brand{left:90px;top:73px;display:flex;align-items:center;gap:12px;font-size:27px;line-height:32px;font-weight:700}
.f-mark{width:54px;height:54px;border:3px solid var(--white);border-radius:4px}
.f-h{font-size:17px;font-weight:700}
.f-link{font-size:14px}
.news-input{left:90px;top:266px;width:326px;height:38px;border-bottom:1px solid #8d9ab0;font-size:13px;color:#b7c0cf;padding-top:12px}
.news-go{left:377px;top:266px;width:39px;height:38px;background:var(--white);display:flex;align-items:center;justify-content:center}
.social{width:28px;height:28px;border-radius:50%;background:var(--white)}
.f-rule{left:90px;top:392px;width:1019px;height:1px;background:#8d9ab0}
.f-bottom{top:418px;font-size:17px}
</style>
</head>
<body>

<!-- navigation -->
<div class="abs brand"><span class="brand-mark"></span><span>Mireval Stone<br>Development</span></div>
<nav class="abs nav">
  <a style="left:770px">Home</a>
  <a style="left:849px">About</a>
  <a style="left:931px">News</a>
</nav>
<div class="abs btn-outline">Contact Us</div>

<!-- hero -->
<section class="abs hero">
  <div class="hero-photo" role="img" aria-label="White modern apartment building with cantilevered floors against a clear sky"></div>
  <h1 class="abs head hero-title">Dorian Vale<br>Ashcombe</h1>
  <p class="abs hero-sub">International Asset Development</p>
  <div class="abs search">
    <div class="search-field" style="left:20px">
      <span class="ico-ring"><svg width="20" height="20" viewBox="0 0 20 20" fill="none" stroke="#0a1f40" stroke-width="1.7"><path d="M5 1v14h14M1 5h14v14"/></svg></span>
      <div><div class="field-label">Building area</div><div class="field-value">Any Size ⌄</div></div>
    </div>
    <div class="search-field" style="left:187px">
      <span class="ico-ring"><svg width="20" height="20" viewBox="0 0 20 20" fill="none" stroke="#0a1f40" stroke-width="1.7"><path d="M2 10l8-8h7v7l-8 8z"/><circle cx="13.5" cy="6.5" r="1.3"/></svg></span>
      <div><div class="field-label">Price range</div><div class="field-value">Any Price ⌄</div></div>
    </div>
    <div class="search-btn">Search</div>
  </div>
</section>

<h2 class="abs head section-title">MIREVAL STONE DEVELOPMENT</h2>

<!-- about -->
<section class="abs about">
  <div class="abs vert">ABOUT US</div>
  <div class="stat" style="left:86px"><div class="stat-num">02</div><div class="stat-label">Partners</div></div>
  <div class="stat" style="left:260px"><div class="stat-num">06</div><div class="stat-label">Employees</div></div>
  <div class="stat" style="left:434px"><div class="stat-num">33</div><div class="stat-label">Investments</div></div>
  <div class="abs eyebrow">Our Expertise</div>
  <h3 class="abs head about-head">Committed to the fundamentals of investing, to ensure long term growth</h3>
  <div class="abs btn-dark" style="left:86px;top:357px;width:112px;height:34px">Contact now</div>
  <div class="abs feature" role="img" aria-label="Glass apartment towers seen from below">
    <div class="abs feature-tag">Industry 01</div>
    <div class="abs head feature-title">Apartment Building<br>Optimization</div>
    <div class="abs feature-btn">Learn More</div>
  </div>
  <span class="dot" style="top:215px;background:var(--navy)"></span>
  <span class="dot" style="top:231px"></span>
  <span class="dot" style="top:248px"></span>
</section>

<!-- properties -->
<h2 class="abs head row-title" style="top:1411px">Current Offered Properties</h2>
<div class="abs explore" style="top:1413px">Explore more <span>→</span></div>

<article class="abs card" style="left:90px">
  <div class="card-photo" role="img" aria-label="Modern house terrace with a fire pit at dusk" style="background:linear-gradient(180deg,#1f47a0 0%,#3a5d8c 40%,#6a6a6a 75%,#9b8f83 100%)"></div>
  <div class="card-title" style="top:396px">Bold and Breathtaking</div>
  <div class="pill" style="left:13px;top:437px"><svg width="11" height="13" viewBox="0 0 11 13" fill="none" stroke="#0b4fa8" stroke-width="1.2"><path d="M5.5 12s4.5-4 4.5-7a4.5 4.5 0 0 0-9 0c0 3 4.5 7 4.5 7z"/><circle cx="5.5" cy="5" r="1.5"/></svg>San Diego</div>
  <div class="meta" style="left:205px;top:441px"><svg width="18" height="16" viewBox="0 0 18 16" fill="none" stroke="#0a1f40" stroke-width="1.4"><path d="M9 15S1 10 1 5a4 4 0 0 1 8-1 4 4 0 0 1 8 1c0 5-8 10-8 10z"/></svg>32</div>
  <div class="meta" style="left:270px;top:441px"><svg width="17" height="16" viewBox="0 0 17 16" fill="none" stroke="#0a1f40" stroke-width="1.4"><path d="M8.5 1a7 6.5 0 1 1-3.5 12L1 15l1.5-3.5A7 6.5 0 0 1 8.5 1z"/></svg>10</div>
</article>

<article class="abs card" style="left:437px">
  <div class="card-photo" role="img" aria-label="Dining room with floor-to-ceiling windows over a city view" style="height:266px;background:linear-gradient(180deg,#6f5a44 0%,#2a4f8a 25%,#53657a 55%,#c8c4bd 100%)"></div>
  <div class="card-title" style="left:14px;top:284px">Bold and Breathtaking</div>
  <div class="abs" style="left:14px;top:328px;font-size:12px;font-weight:600;color:var(--navy)">Offered at <span style="font-size:20px;font-weight:600;margin-left:3px">$2,499,000</span></div>
  <p class="abs" style="left:14px;top:363px;width:300px;font-size:12px;line-height:14px;color:var(--navy)">With sharp clean lines, and attention paid to every detail, you will quickly see why 4410 Linden Ave.</p>
  <div class="pill" style="left:13px;top:437px"><svg width="11" height="13" viewBox="0 0 11 13" fill="none" stroke="#0b4fa8" stroke-width="1.2"><path d="M5.5 12s4.5-4 4.5-7a4.5 4.5 0 0 0-9 0c0 3 4.5 7 4.5 7z"/><circle cx="5.5" cy="5" r="1.5"/></svg>San Diego</div>
  <div class="pill" style="left:125px;top:437px"><svg width="12" height="12" viewBox="0 0 12 12" fill="none" stroke="#0b4fa8" stroke-width="1.2"><path d="M3 1v8h8M1 3h8v8"/></svg>2,136 Sq Ft.</div>
  <div class="abs" style="left:268px;top:427px;width:44px;height:44px;border-radius:50%;background:var(--navy);display:flex;align-items:center;justify-content:center"><svg width="18" height="18" viewBox="0 0 18 18" fill="none" stroke="#fff" stroke-width="2"><path d="M3 15L15 3M6 3h9v9"/></svg></div>
</article>

<article class="abs card" style="left:783px">
  <div class="card-photo" role="img" aria-label="Bright open-plan interior with wood ceiling and kitchen" style="background:linear-gradient(160deg,#8a6a4c 0%,#d9dadb 30%,#eeeeee 55%,#b8a58f 80%,#2a3440 100%)"></div>
  <div class="card-title" style="top:396px">Bold and Breathtaking</div>
  <div class="pill" style="left:13px;top:437px"><svg width="11" height="13" viewBox="0 0 11 13" fill="none" stroke="#0b4fa8" stroke-width="1.2"><path d="M5.5 12s4.5-4 4.5-7a4.5 4.5 0 0 0-9 0c0 3 4.5 7 4.5 7z"/><circle cx="5.5" cy="5" r="1.5"/></svg>San Diego</div>
  <div class="meta" style="left:205px;top:441px"><svg width="18" height="16" viewBox="0 0 18 16" fill="none" stroke="#0a1f40" stroke-width="1.4"><path d="M9 15S1 10 1 5a4 4 0 0 1 8-1 4 4 0 0 1 8 1c0 5-8 10-8 10z"/></svg>32</div>
  <div class="meta" style="left:270px;top:441px"><svg width="17" height="16" viewBox="0 0 17 16" fill="none" stroke="#0a1f40" stroke-width="1.4"><path d="M8.5 1a7 6.5 0 1 1-3.5 12L1 15l1.5-3.5A7 6.5 0 0 1 8.5 1z"/></svg>10</div>
</article>

<!-- news -->
<h2 class="abs head row-title" style="top:2060px">News</h2>
<div class="abs explore" style="top:2061px">Explore more <span>→</span></div>

<article class="abs news" style="left:90px" role="img" aria-label="Family portrait outdoors for a rental demographics article">
  <div style="position:absolute;inset:0;background:linear-gradient(180deg,#c9d3d6 0%,#9aa6a8 35%,#7f98b5 60%,var(--sky) 100%)"></div>
  <div class="news-title" style="top:232px">Exploring US Single-Family<br>Rental Demographics</div>
  <div class="news-meta"><span>▭ August 20, 2022</span><span>◉ 70 views</span></div>
</article>
<article class="abs news" style="left:437px" role="img" aria-label="Team sketching plans on a whiteboard">
  <div style="position:absolute;inset:0;background:linear-gradient(180deg,#d8dadd 0%,#b8b1aa 35%,#8ba3c2 65%,var(--sky) 100%)"></div>
  <div class="news-title" style="top:256px">2023 ESG Report</div>
  <div class="news-meta"><span>▭ July 20, 2024</span><span>◉ 70 views</span></div>
</article>
<article class="abs news" style="left:783px" role="img" aria-label="Small model house beside a savings jar">
  <div style="position:absolute;inset:0;background:linear-gradient(180deg,#d9c9c4 0%,#b7a7a3 35%,#8fa9c9 65%,var(--sky) 100%)"></div>
  <div class="news-title" style="top:232px">2024 Mid-Year Global<br>Investment Outlook</div>
  <div class="news-meta"><span>▭ June 20, 2024</span><span>◉ 70 views</span></div>
</article>

<!-- contact -->
<section class="abs form-card">
  <h3 class="abs head form-title">Send Us a Message</h3>
  <p class="abs form-sub">You can reach us anytime</p>
  <div class="input" style="left:26px;top:133px;width:214px;height:42px">*Name</div>
  <div class="input" style="left:259px;top:133px;width:214px;height:42px">*Email</div>
  <div class="input" style="left:26px;top:196px;width:447px;height:136px">Message</div>
  <div class="abs btn-dark submit">Submit</div>
  <p class="abs legal">By contacting us, you agree to our <b>Terms of service</b><br>and <b>Privacy Policy</b></p>
</section>

<h3 class="abs head inquiry">For any inquiries, please call or email us. Alternatively you can fill in the following contact form</h3>
<div class="contact-item" style="top:2757px"><span class="ci-box"><svg width="22" height="22" viewBox="0 0 22 22" fill="none" stroke="#0b4fa8" stroke-width="1.4"><path d="M4 2h4l2 5-2.5 1.5a11 11 0 0 0 6 6L15 12l5 2v4a2 2 0 0 1-2 2A16 16 0 0 1 2 4a2 2 0 0 1 2-2z"/></svg></span>+ (555) 014-2870</div>
<div class="contact-item" style="top:2825px"><span class="ci-box"><svg width="24" height="18" viewBox="0 0 24 18" fill="none" stroke="#0b4fa8" stroke-width="1.4"><rect x="1" y="1" width="22" height="16" rx="1"/><path d="M1 2l11 8 11-8M1 16l8-7M23 16l-8-7"/></svg></span>hello@mirevalstone-homes.com</div>
<div class="contact-item" style="top:2890px"><span class="ci-box"><svg width="24" height="18" viewBox="0 0 24 18" fill="none" stroke="#0b4fa8" stroke-width="1.4"><rect x="1" y="1" width="22" height="16" rx="3"/><path d="M9 17V7a4 4 0 0 0-8 0M14 8h5"/></svg></span>1480 Harbor Crest Ave #310 San Diego CA. 92117</div>

<!-- footer -->
<footer class="abs footer">
  <div class="abs f-brand"><span class="f-mark"></span><span>Mireval Stone<br>Development</span></div>
  <div class="abs f-h" style="left:90px;top:218px">Subsscribe to our newsletter</div>
  <div class="abs news-input">Email address</div>
  <div class="abs news-go"><svg width="20" height="18" viewBox="0 0 20 18" fill="none" stroke="#0a1f40" stroke-width="2"><path d="M1 9h17M11 2l7 7-7 7"/></svg></div>
  <div class="abs f-h" style="left:524px;top:218px">Menu</div>
  <div class="abs f-link" style="left:524px;top:264px">About</div>
  <div class="abs f-link" style="left:524px;top:300px">News</div>
  <div class="abs f-link" style="left:524px;top:336px">Contact Us</div>
  <div class="abs f-h" style="left:783px;top:221px">Social Media</div>
  <span class="abs social" style="left:783px;top:261px" aria-label="Social link"></span>
  <span class="abs social" style="left:850px;top:261px" aria-label="Social link"></span>
  <span class="abs social" style="left:916px;top:261px" aria-label="Social link"></span>
  <div class="abs f-rule"></div>
  <div class="abs f-bottom" style="left:90px">Term &amp; Conditions</div>
  <div class="abs f-bottom" style="left:294px">Privacy Policy</div>
</footer>

</body>
</html>
```